Historic Church website

We want our church website to feel warm, historic, and clean, modern, and easy to navigate. Dont use the anchor

Current website: https://www.meadowlarkfellowship.org/

Requirements
Should not have
• I would like to use the logo without the anchor

```html
<!DOCTYPE html>
<html lang="en">
<head>
<meta charset="utf-8">
<title>Meadowlark Fellowship</title>
<link rel="stylesheet" href="https://fonts.googleapis.com/css2?family=EB+Garamond:ital,wght@0,400;0,500;0,600;1,400&display=swap">
<style>
:root{
  --bg:#2e2d33;
  --bg-deep:#242328;
  --panel:#38373e;
  --line:#4a4951;
  --gold:#b8965e;
  --text:#ecebe8;
  --muted:#bdbbb6;
  --white:#ffffff;
  --ink:#2a2a2e;
}
*{box-sizing:border-box;margin:0;padding:0}
html,body{width:1200px;height:5094px;overflow:hidden}
body{background:var(--bg);color:var(--text);font-family:"EB Garamond",Georgia,serif;position:relative}
section,header,footer{position:relative;width:1200px;overflow:hidden}
.abs{position:absolute}
.brand{display:flex;align-items:center;gap:12px;color:var(--text);font-size:22px;font-weight:500;letter-spacing:.04em}
.brand .dot{width:30px;height:30px;border:2px solid var(--text);border-radius:50%}
.btn{position:absolute;display:flex;align-items:center;justify-content:center;font-size:12px;font-weight:600;letter-spacing:.06em}
.btn-gold{background:var(--gold);color:var(--white)}
.btn-line{border:2px solid var(--text);color:var(--text)}
h2.title{font-weight:400;font-size:44px;letter-spacing:.02em;color:var(--text)}

/* hero */
.hero{height:666px}
.hero-photo{position:absolute;inset:0;background:radial-gradient(ellipse at 50% 45%,#3c4a6a 0%,#24304a 40%,#1a2033 75%,#2a2c36 100%)}
.hero-shade{position:absolute;inset:0;background:linear-gradient(180deg,rgba(20,22,30,.35),rgba(30,32,40,.55) 70%,rgba(46,45,51,.9))}
.nav{position:absolute;top:96px;left:261px;display:flex;gap:30px;font-size:11px;letter-spacing:.08em;color:var(--muted)}
.donate{left:810px;top:91px;width:127px;height:32px;border:1.5px solid var(--muted);color:var(--text);font-size:11px;letter-spacing:.12em}
.hero h1{position:absolute;top:330px;width:100%;text-align:center;font-weight:400;font-size:58px;letter-spacing:.03em}
.hero .lede{position:absolute;top:418px;left:290px;width:620px;text-align:center;font-size:18px;line-height:32px;color:#dedcd7}
.tagline{height:69px;border-top:1px solid var(--line);border-bottom:1px solid var(--line);text-align:center;font-size:16px;letter-spacing:.45em;line-height:67px;color:var(--text)}

/* rooted */
.rooted{height:418px;border-bottom:1px solid var(--line)}
.rooted .divider{left:615px;top:0;width:1px;height:418px;background:var(--line)}
.rooted h2{position:absolute;left:140px;top:74px}
.rooted p{position:absolute;left:140px;top:155px;width:400px;font-size:14.5px;line-height:27px;color:#d6d4cf}
.rooted-photo{left:686px;top:50px;width:372px;height:312px;background:linear-gradient(135deg,#6c6466 0%,#4a4347 45%,#2c2a2e 100%)}

/* gatherings */
.gatherings{height:554px;margin-top:19px}
.gatherings-photo{position:absolute;inset:0;background:linear-gradient(180deg,#4b4a55,#3d3c46 60%,#34333a)}
.gatherings h2{position:absolute;top:70px;width:100%;text-align:center}
.g-card{position:absolute;top:156px;width:291px;height:309px;background:rgba(42,41,47,.92);text-align:center}
.g-icon{width:70px;height:70px;border:1.5px solid var(--gold);border-radius:50%;margin:30px auto 0;display:flex;align-items:center;justify-content:center}
.g-card h3{font-weight:400;font-size:19px;line-height:28px;margin-top:24px}
.g-time{color:var(--gold);font-size:15px;margin-top:16px;display:inline-block;border-bottom:1px solid var(--gold);padding-bottom:2px}
.g-card p{font-size:13px;line-height:22px;color:var(--muted);margin:16px auto 0;width:200px}

/* events */
.events{height:567px}
.events h2{position:absolute;left:140px;top:80px}
.arrow{position:absolute;top:93px;width:40px;height:40px;border:1px solid var(--muted);border-radius:50%;display:flex;align-items:center;justify-content:center}
.events-photo{left:140px;top:164px;width:457px;height:397px;background:linear-gradient(180deg,#6b6a8a 0%,#8a7b6a 45%,#4a3f3a 80%,#2e2a2a 100%)}
.event{position:absolute;left:668px;width:390px;border-bottom:1px solid var(--line)}
.event .time{font-size:11px;color:var(--muted);display:flex;gap:6px;align-items:center}
.event h3{font-weight:400;font-size:24px;margin-top:6px}
.event .desc{font-size:11.5px;color:var(--muted);margin-top:8px}
.chips{display:flex;gap:8px;margin-top:12px}
.chips span{font-size:9.5px;color:#8e8c88;border:1px solid var(--line);padding:3px 8px}
.event .loc{font-size:10px;color:var(--muted);margin-top:16px;display:flex;gap:6px;align-items:center;padding-bottom:20px}

/* voices */
.voices{height:850px;margin-top:99px}
.v-back{left:117px;top:20px;width:686px;height:712px;background:var(--bg-deep)}
.v-frame{left:137px;top:0;width:638px;height:144px;border:1.5px solid var(--gold);border-bottom:none}
.voices h2{position:absolute;top:58px;width:920px;text-align:center;left:0}
.v-wrap{position:absolute;left:-117px;top:0;width:1200px;height:100%}
.quote{position:absolute;width:450px;height:252px;background:var(--white);color:var(--ink);padding:26px 48px}
.quote .mark{font-size:84px;line-height:60px;color:transparent;-webkit-text-stroke:1.5px var(--gold);font-family:"EB Garamond",serif;height:46px;overflow:hidden}
.quote blockquote{font-style:italic;font-size:19px;line-height:30px;margin-top:24px;height:94px}
.quote cite{font-style:normal;font-size:12px;letter-spacing:.08em;display:flex;align-items:center;gap:12px;margin-top:12px}
.quote cite::before{content:"";width:32px;height:1px;background:var(--gold)}

/* sermons */
.sermons{height:756px;margin-top:5px}
.sermons-photo{position:absolute;inset:0;background:radial-gradient(ellipse at 65% 55%,#48474e,#323137 55%,#26252a)}
.sermons h2{position:absolute;left:150px;top:76px}
.sermons .aside{position:absolute;left:779px;top:84px;width:260px;font-size:15px;line-height:26px;color:#d6d4cf}
.s-row{position:absolute;left:148px;width:910px;border:1px solid #5a5960;background:rgba(40,39,45,.55)}
.s-row .series{position:absolute;left:42px;top:22px;font-size:10px;color:var(--gold);letter-spacing:.05em}
.s-row h3{position:absolute;left:42px;top:38px;font-weight:400;font-size:23px;line-height:23px}
.s-row .by{position:absolute;left:42px;font-size:10.5px;color:var(--muted);display:flex;align-items:center;gap:8px}
.s-row .by i{width:16px;height:16px;border-radius:50%;background:var(--gold);display:inline-block}
.s-row .date{position:absolute;left:578px;font-size:10.5px;color:var(--muted);display:flex;gap:6px;align-items:center}
.play{position:absolute;left:826px;width:51px;height:51px;background:var(--gold);display:flex;align-items:center;justify-content:center}
.library{left:482px;top:623px;width:234px;height:51px;border:1.5px solid var(--text);color:var(--text)}

/* connect */
.connect{height:465px;background:var(--bg)}
.connect h2{position:absolute;top:100px;width:100%;text-align:center}
.connect p{position:absolute;top:186px;left:300px;width:600px;text-align:center;font-size:15px;line-height:27px;color:#d6d4cf}
.email{position:absolute;left:275px;top:267px;width:506px;height:54px;border:1px solid #5a5960;font-size:12px;color:#8e8c88;padding-left:34px;line-height:52px}
.subscribe{left:793px;top:267px;width:130px;height:54px}
.connect .note{position:absolute;top:349px;width:100%;text-align:center;font-size:12px;color:var(--muted)}

/* footer */
.site-footer{height:626px;background:linear-gradient(180deg,var(--bg),#29282d)}
.site-footer .brand{position:absolute;left:0;width:100%;justify-content:center;top:70px}
.f-col{position:absolute;top:192px}
.f-col h4{font-weight:500;font-size:15px;padding-bottom:8px;position:relative}
.f-col h4::after{content:"";position:absolute;left:0;bottom:0;width:44px;height:1px;background:var(--gold)}
.f-col ul{list-style:none;margin-top:18px}
.f-col li{font-size:11px;color:var(--muted);line-height:31px}
.contact li{display:flex;gap:12px;align-items:flex-start;line-height:18px;margin-bottom:14px}
.socials{position:absolute;left:150px;top:372px;display:flex;gap:16px}
.socials span{width:30px;height:30px;border:1px solid #5a5960;display:flex;align-items:center;justify-content:center}
.socials span b{width:10px;height:10px;border:1.5px solid var(--gold);border-radius:50%}
.f-rule{left:150px;top:458px;width:908px;height:1px;background:var(--line)}
.f-bottom{position:absolute;top:476px;left:150px;width:908px;display:flex;justify-content:space-between;font-size:10.5px;color:var(--muted)}
</style>
</head>
<body>

<header class="hero">
  <div class="hero-photo" role="img" aria-label="Grand historic library hall with tall wooden bookshelves in blue evening light"></div>
  <div class="hero-shade"></div>
  <div class="brand abs" style="left:0;width:100%;justify-content:center;top:22px"><span class="dot"></span>Meadowlark Fellowship</div>
  <nav class="nav"><span>ABOUT MF</span><span>MINISTRIES</span><span>BIBLE STUDIES</span><span>SERMON LIBRARY</span></nav>
  <a class="btn donate">DONATE</a>
  <h1>Meadowlark Fellowship</h1>
  <p class="lede">An independent Christian church in the Protestant tradition dedicated to the faithful study and proclamation of God's Word.</p>
  <a class="btn btn-gold" style="left:366px;top:536px;width:199px;height:51px">Visit Us This Sunday</a>
  <a class="btn btn-line" style="left:593px;top:536px;width:241px;height:51px">Watch This Week's Sermon</a>
</header>

<div class="tagline">FAITH IN CHRIST. LIFE IN THE WORD.</div>

<section class="rooted">
  <div class="abs divider"></div>
  <h2 class="title">Rooted in Scripture</h2>
  <p>Meadowlark Fellowship is an independent Christian church in the Protestant tradition. We believe the entire Bible is the inspired and inerrant Word of God, the Trinity, Christ's perfect life, atoning death, bodily resurrection and ascension, and our need for salvation through personal faith in Jesus Christ.</p>
  <div class="abs rooted-photo" role="img" aria-label="Open Bible resting on a wooden table in soft window light"></div>
</section>

<section class="gatherings">
  <div class="gatherings-photo" role="img" aria-label="Dim library reading room with shelves and tables"></div>
  <h2 class="title">Weekly Gatherings</h2>
  <div class="g-card" style="left:140px">
    <div class="g-icon"><svg width="34" height="30" viewBox="0 0 34 30" fill="none" stroke="#b8965e" stroke-width="1.4"><path d="M8 20a9 9 0 0 1 18 0"/><path d="M2 24h30M17 3v5M6 9l3 3M28 9l-3 3M12 27h10"/></svg></div>
    <h3>Morning Worship<br>Service</h3>
    <span class="g-time">11:00 AM</span>
    <p>Join us for reverent worship, corporate prayer, hymn singing, and the faithful exposition of Scripture.</p>
  </div>
  <div class="g-card" style="left:454px">
    <div class="g-icon"><svg width="36" height="30" viewBox="0 0 36 30" fill="none" stroke="#b8965e" stroke-width="1.4"><path d="M8 26h20a6 6 0 0 0 0-12 9 9 0 0 0-17-2 7 7 0 0 0-3 14z"/><circle cx="27" cy="7" r="4"/></svg></div>
    <h3>All Church<br>Lunch</h3>
    <span class="g-time">12:15 PM</span>
    <p>Break bread together as we fellowship and build community around the table each Lord's Day.</p>
  </div>
  <div class="g-card" style="left:767px">
    <div class="g-icon"><svg width="34" height="28" viewBox="0 0 34 28" fill="none" stroke="#b8965e" stroke-width="1.4"><path d="M17 6c-4-3-9-3-14-2v19c5-1 10-1 14 2 4-3 9-3 14-2V4c-5-1-10-1-14 2zM17 6v19"/></svg></div>
    <h3>Afternoon Adult<br>Bible Study</h3>
    <span class="g-time">12:45 PM</span>
    <p>Dive deeper into God's Word through systematic study, discussion, and application for daily living.</p>
  </div>
</section>

<section class="events">
  <h2 class="title">Upcoming Events</h2>
  <span class="arrow" style="left:966px"><svg width="10" height="10" viewBox="0 0 10 10" fill="none" stroke="#ecebe8" stroke-width="1.3"><path d="M6 2L3 5l3 3"/></svg></span>
  <span class="arrow" style="left:1018px"><svg width="10" height="10" viewBox="0 0 10 10" fill="none" stroke="#ecebe8" stroke-width="1.3"><path d="M4 2l3 3-3 3"/></svg></span>
  <div class="abs events-photo" role="img" aria-label="Two students standing before tall stained glass windows"></div>
  <div class="event" style="top:196px">
    <div class="time"><svg width="11" height="11" viewBox="0 0 11 11" fill="none" stroke="#b8965e"><circle cx="5.5" cy="5.5" r="4.5"/><path d="M5.5 3v3h2"/></svg>11:00 AM</div>
    <h3>Sunday Service</h3>
    <div class="desc">Review church business and pray together for our ministry</div>
    <div class="chips"><span>January 26</span><span>February 2</span><span>February 9</span><span>February 16</span></div>
    <div class="loc"><svg width="9" height="12" viewBox="0 0 9 12" fill="none" stroke="#b8965e"><path d="M4.5 11S1 7 1 4.5a3.5 3.5 0 0 1 7 0C8 7 4.5 11 4.5 11z"/></svg>Northeast corner of Elm St. and Harbor Rd., Fairhaven, OR</div>
  </div>
  <div class="event" style="top:392px">
    <div class="time"><svg width="11" height="11" viewBox="0 0 11 11" fill="none" stroke="#b8965e"><circle cx="5.5" cy="5.5" r="4.5"/><path d="M5.5 3v3h2"/></svg>7:30 PM</div>
    <h3>Wednesday Night Bible Study</h3>
    <div class="desc">Review church business and pray together for our ministry</div>
    <div class="chips"><span>January 22</span><span>January 29</span><span>February 5</span><span>February 12</span></div>
    <div class="loc"><svg width="9" height="12" viewBox="0 0 9 12" fill="none" stroke="#b8965e"><path d="M4.5 11S1 7 1 4.5a3.5 3.5 0 0 1 7 0C8 7 4.5 11 4.5 11z"/></svg>Northwest corner of Elm St. and Harbor Rd., Fairhaven, OR</div>
  </div>
</section>

<section class="voices">
  <div class="abs v-back" style="left:257px;top:20px"></div>
  <div class="abs v-frame" style="left:277px"></div>
  <h2 class="title" style="position:absolute;top:58px;left:0;width:1200px;text-align:center">Voices of Faith</h2>
  <div class="quote" style="left:140px;top:144px">
    <div class="mark">&#8221;</div>
    <blockquote>Christians are called to God's service not only in church professions but also in every secular calling...</blockquote>
    <cite>J. Harlan Whitcombe</cite>
  </div>
  <div class="quote" style="left:609px;top:144px">
    <div class="mark">&#8221;</div>
    <blockquote>To all who worship with us we extend a cordial welcome...</blockquote>
    <cite>Amos T. Brandell</cite>
  </div>
  <div class="quote" style="left:140px;top:415px">
    <div class="mark">&#8221;</div>
    <blockquote>The great need across evangelicalism is exposition of the Scriptures...</blockquote>
    <cite>R. Elliot Marchbank</cite>
  </div>
  <div class="quote" style="left:609px;top:415px">
    <div class="mark">&#8221;</div>
    <blockquote>We must meet the present situation, and we must speak a word to the world...</blockquote>
    <cite>G. Lyndon Ashworth</cite>
  </div>
</section>

<section class="sermons">
  <div class="sermons-photo" role="img" aria-label="Dim study with an old lamp and open books"></div>
  <h2 class="title">Upcoming Events</h2>
  <p class="aside">Faithful exposition of God's Word, Sunday by Sunday</p>
  <div class="s-row" style="top:166px;height:126px">
    <span class="series">Revelation Series</span>
    <h3>Blind, Bare and Bankrupt</h3>
    <span class="by" style="top:80px"><i></i>Pastor Samuel Everly</span>
    <span class="date" style="top:56px"><svg width="11" height="11" viewBox="0 0 11 11" fill="none" stroke="#b8965e"><rect x="1" y="2" width="9" height="8"/><path d="M1 5h9M3 1v2M8 1v2"/></svg>January 19, 2026</span>
    <span class="play" style="top:37px"><svg width="16" height="18" viewBox="0 0 16 18"><path d="M2 1l13 8-13 8z" fill="#2e2d33"/></svg></span>
  </div>
  <div class="s-row" style="top:307px;height:125px">
    <span class="series">Revelation Series</span>
    <h3>Small in Strength, Strong in Faith</h3>
    <span class="by" style="top:80px"><i></i>Pastor Samuel Everly</span>
    <span class="date" style="top:56px"><svg width="11" height="11" viewBox="0 0 11 11" fill="none" stroke="#b8965e"><rect x="1" y="2" width="9" height="8"/><path d="M1 5h9M3 1v2M8 1v2"/></svg>January 12, 2026</span>
    <span class="play" style="top:37px"><svg width="16" height="18" viewBox="0 0 16 18"><path d="M2 1l13 8-13 8z" fill="#2e2d33"/></svg></span>
  </div>
  <div class="s-row" style="top:447px;height:134px">
    <span class="series">Revelation Series</span>
    <h3>Letters to the Church in Fairhaven:<br>Sardis - Alive by Name, Dead in Truth</h3>
    <span class="by" style="top:104px"><i></i>Pastor Samuel Everly</span>
    <span class="date" style="top:61px"><svg width="11" height="11" viewBox="0 0 11 11" fill="none" stroke="#b8965e"><rect x="1" y="2" width="9" height="8"/><path d="M1 5h9M3 1v2M8 1v2"/></svg>January 5, 2026</span>
    <span class="play" style="top:41px"><svg width="16" height="18" viewBox="0 0 16 18"><path d="M2 1l13 8-13 8z" fill="#2e2d33"/></svg></span>
  </div>
  <a class="btn library">View Full Sermon Library</a>
</section>

<section class="connect">
  <h2 class="title">Stay Connected</h2>
  <p>Receive our weekly newsletter with sermon notes, upcoming events, and resources for spiritual growth. We respect your privacy and will never share your information.</p>
  <div class="email">Enter your email address</div>
  <a class="btn btn-gold subscribe">Subscribe</a>
  <div class="note">We respect your privacy. Unsubscribe at any time.</div>
</section>

<footer class="site-footer">
  <div class="brand"><span class="dot"></span>Meadowlark Fellowship</div>
  <div class="f-col contact" style="left:150px">
    <h4>Contact</h4>
    <ul>
      <li><svg width="9" height="12" viewBox="0 0 9 12" fill="none" stroke="#b8965e"><path d="M4.5 11S1 7 1 4.5a3.5 3.5 0 0 1 7 0C8 7 4.5 11 4.5 11z"/></svg><span>2140 Meadowlark Lane<br>Fairhaven, Oregon 97401</span></li>
      <li><svg width="11" height="11" viewBox="0 0 11 11" fill="none" stroke="#b8965e"><path d="M2 1h2l1 3-1.5 1a6 6 0 0 0 2.5 2.5L7 6l3 1v2a1 1 0 0 1-1 1A8 8 0 0 1 1 2a1 1 0 0 1 1-1z"/></svg><span>541.555.0192</span></li>
      <li><svg width="12" height="10" viewBox="0 0 12 10" fill="none" stroke="#b8965e"><rect x="1" y="1" width="10" height="8"/><path d="M1 1l5 4 5-4"/></svg><span>info@meadowlarkfellowship.org</span></li>
    </ul>
  </div>
  <div class="socials"><span aria-label="Social link"><b></b></span><span aria-label="Social link"><b></b></span><span aria-label="Social link"><b></b></span></div>
  <div class="f-col" style="left:445px"><h4>About</h4><ul><li>Our History</li><li>What We Believe</li><li>Our Pastors</li><li>Join Us</li></ul></div>
  <div class="f-col" style="left:619px"><h4>Ministries</h4><ul><li>Children</li><li>Youth</li><li>College &amp; Young Adults</li><li>Women's Ministry</li><li>Men's Ministry</li></ul></div>
  <div class="f-col" style="left:852px"><h4>Resources</h4><ul><li>Sermon Library</li><li>Bible Studies</li><li>Recommended Reading</li><li>Contact Us</li></ul></div>
  <div class="abs f-rule"></div>
  <div class="f-bottom"><span>© 2026 Meadowlark Fellowship. All rights reserved.</span><span>Privacy Policy &nbsp;/&nbsp; Terms of Use</span></div>
</footer>

</body>
</html>
```